Site for a workout and Consulting enterprise

I need a professional responsive site for www.olvaru.hamburg. The website shoulderstand consist of a Landing and 4 other pages. - On page for the contact informations - on page for the about - on page for consulting services (technical) - on page for Training and workshop services (business and soft skills) I add some files so you can see my idea of the design.
Target Market(s)
IT and Management
Industry/Entity Type
Management Consulting
Coding
Coded - Design and coding required
Number of Pages Required
4 page
Requirements
Must have
- Use Pictures for Background, Sliders and Topics. Just have to placeholders for the design.

```html
<!DOCTYPE html>
<html lang="de">
<head>
<meta charset="utf-8">
<title>olvaru – Individuen, Ideen, Innovationen</title>
<link rel="stylesheet" href="https://fonts.googleapis.com/css2?family=Roboto:wght@300;400;500&display=swap">
<style>
  :root {
    --bg-dark: #3b3426;
    --bg-mid: #6b5a3c;
    --bg-warm: #8a6a40;
    --bg-green: #5f6a48;
    --panel: rgba(225, 228, 232, 0.22);
    --white: #ffffff;
    --text-soft: rgba(255, 255, 255, 0.85);
    --step-one: #13977f;
    --step-two: #47b04b;
    --step-three: #16b4d2;
    --accent-blue: #3b4dc8;
    --disc: #4a4036;
    --link: #c8e02a;
  }
  * { margin: 0; padding: 0; box-sizing: border-box; }
  html, body { width: 1200px; height: 663px; overflow: hidden; }
  body { font-family: "Roboto", Arial, sans-serif; color: var(--white); }

  .landing { position: relative; width: 1200px; height: 663px; overflow: hidden; }

  .hero-photo {
    position: absolute; inset: 0;
    background:
      radial-gradient(ellipse at 30% 25%, rgba(160,170,140,0.55), transparent 55%),
      linear-gradient(180deg, var(--bg-green) 0%, var(--bg-mid) 40%, var(--bg-warm) 65%, var(--bg-dark) 100%);
  }

  .brand { position: absolute; left: 106px; top: 292px; }
  .brand-name { font-size: 100px; font-weight: 400; line-height: 1; letter-spacing: 1px; }
  .brand-tagline { margin-top: 6px; font-size: 27px; font-weight: 300; }

  .info-panel {
    position: absolute; left: 600px; top: 25px; width: 574px; height: 622px;
    background: var(--panel);
  }

  .toggle {
    position: absolute; left: 570px; top: 269px; width: 134px; height: 134px;
  }

  .step { position: absolute; display: flex; align-items: center; }
  .step-badge {
    width: 74px; height: 74px; border-radius: 50%;
    display: flex; align-items: center; justify-content: center;
    font-size: 26px; font-weight: 400; flex-shrink: 0;
  }
  .step-one .step-badge { background: var(--step-one); }
  .step-two .step-badge { background: var(--step-two); }
  .step-three .step-badge { background: var(--step-three); }
  .step-text { margin-left: 22px; }
  .step-title { font-size: 18px; font-weight: 500; margin-bottom: 8px; }
  .step-line { font-size: 15px; font-weight: 400; color: var(--text-soft); line-height: 20px; }

  .step-one { left: 684px; top: 180px; }
  .step-two { left: 732px; top: 299px; }
  .step-three { left: 684px; top: 419px; }

  .footer-links {
    position: absolute; left: 600px; width: 574px; top: 612px;
    text-align: center; font-size: 14px; color: var(--link);
  }
  .footer-links a { color: var(--link); text-decoration: none; }
  .footer-links .divider { margin: 0 6px; color: var(--text-soft); }
</style>
</head>
<body>
<main class="landing">
  <div class="hero-photo" role="img" aria-label="Hintergrundfoto: Bahngleise mit Herbstlaub und einer alten Weichenstellvorrichtung"></div>

  <div class="brand">
    <div class="brand-name">olvaru</div>
    <div class="brand-tagline">Individuen, Ideen, Innovationen</div>
  </div>

  <section class="info-panel" aria-label="Leistungen"></section>

  <svg class="toggle" viewBox="0 0 134 134" aria-hidden="true">
    <circle cx="67" cy="67" r="66" fill="var(--disc)"/>
    <path d="M67 1 A66 66 0 0 0 67 133 Z" fill="var(--accent-blue)"/>
    <path d="M67 52 V82 M52 67 H82" stroke="var(--white)" stroke-width="2.5"/>
  </svg>

  <div class="step step-one">
    <div class="step-badge">1</div>
    <div class="step-text">
      <div class="step-title">Lorem Ipsum is dummy text</div>
      <div class="step-line">Lorem Ipsum is dummy text</div>
      <div class="step-line">Lorem Ipsum is dummy text</div>
    </div>
  </div>

  <div class="step step-two">
    <div class="step-badge">2</div>
    <div class="step-text">
      <div class="step-title">Lorem Ipsum is dummy text</div>
      <div class="step-line">Lorem Ipsum is dummy text</div>
      <div class="step-line">Lorem Ipsum is dummy text</div>
    </div>
  </div>

  <div class="step step-three">
    <div class="step-badge">3</div>
    <div class="step-text">
      <div class="step-title">Lorem Ipsum is dummy text</div>
      <div class="step-line">Lorem Ipsum is dummy text</div>
      <div class="step-line">Lorem Ipsum is dummy text</div>
    </div>
  </div>

  <nav class="footer-links">
    <a href="#impressum">Impressum</a><span class="divider">|</span><a href="#kontakt">Kontakt</a>
  </nav>
</main>
</body>
</html>
```